Industrial Automation company requires a business card design

Dravel Automation provides design & build of Automated Equipment for manufacturing industry.
www.dravelautomation-example.com
The equipment we design is used for manufacturing in sectors such as medical device, pharmaceutical, aerospace and electronics.
We require a new business card design which incorporates our (New) logo and the key message words:
Automated Equipment:
Design, Build, Control, Test, Support

```html
<!DOCTYPE html>
<html lang="en">
<head>
<meta charset="utf-8">
<title>Dravel Automation – Business Card</title>
<link href="https://fonts.googleapis.com/css2?family=Source+Sans+3:wght@400;600&display=swap" rel="stylesheet">
<style>
  :root {
    --green: #1f844c;
    --charcoal: #333333;
    --white: #ffffff;
    --backdrop: #5b5b5b;
  }
  * { margin: 0; padding: 0; box-sizing: border-box; }
  html, body { width: 1200px; height: 1200px; overflow: hidden; }
  body {
    background: var(--backdrop);
    font-family: "Source Sans 3", sans-serif;
    position: relative;
  }
  .card {
    position: absolute;
    left: 280px;
    width: 640px;
    height: 364px;
    overflow: hidden;
    box-shadow: 0 4px 10px rgba(0,0,0,0.45);
  }
  .card-front { top: 206px; background: var(--white); }
  .card-back { top: 632px; background: var(--charcoal); }
  .card-art { position: absolute; inset: 0; width: 100%; height: 100%; }

  .brand {
    position: absolute;
    display: flex;
    align-items: center;
    gap: 12px;
    color: var(--green);
    font-weight: 600;
    font-size: 34px;
    letter-spacing: 0.5px;
    white-space: nowrap;
  }
  .brand-dot {
    width: 34px; height: 34px;
    border-radius: 50%;
    background: var(--green);
    flex: none;
  }
  .card-front .brand { left: 30px; top: 46px; }
  .card-back .brand { left: 0; right: 0; top: 130px; justify-content: center; font-size: 38px; }
  .card-back .brand-dot { background: var(--white); }

  .person {
    position: absolute;
    right: 32px;
    top: 160px;
    text-align: right;
    color: var(--white);
  }
  .person-name { font-size: 24px; line-height: 28px; }
  .person-role { font-size: 18px; line-height: 22px; }
  .accent-bar {
    position: absolute;
    right: 0; top: 162px;
    width: 12px; height: 46px;
    background: var(--white);
  }

  .address {
    position: absolute;
    left: 38px; top: 284px;
    color: var(--white);
    font-size: 18px;
    line-height: 24px;
  }
  .contact {
    position: absolute;
    right: 32px; top: 260px;
    list-style: none;
    color: var(--white);
    font-size: 18px;
    line-height: 24px;
  }
  .contact li { display: flex; justify-content: flex-end; align-items: center; gap: 14px; }
  .contact svg { width: 19px; height: 17px; flex: none; }

  .tagline {
    position: absolute;
    left: 0; right: 0; top: 260px;
    text-align: center;
    font-size: 18px;
    line-height: 25px;
  }
  .tagline-lead { color: var(--green); }
  .tagline-list { color: var(--white); }
</style>
</head>
<body>

<section class="card card-front">
  <svg class="card-art" viewBox="0 0 800 454" preserveAspectRatio="none" aria-hidden="true">
    <path d="M0,245 C260,240 530,170 640,0 L645,0 C540,185 260,275 0,300 Z" fill="#333333"/>
    <path d="M645,0 L800,0 L800,454 L0,454 L0,300 C260,275 540,185 645,0 Z" fill="#1f844c"/>
    <path d="M0,300 C260,275 540,185 645,0" fill="none" stroke="#ffffff" stroke-width="1.5"/>
  </svg>

  <div class="brand"><span class="brand-dot"></span>Dravel Automation</div>

  <div class="person">
    <p class="person-name">Ciaran Holt</p>
    <p class="person-role">Managing Partner</p>
  </div>
  <div class="accent-bar"></div>

  <p class="address">Glenmara, Kilbrack<br>Co. Westmoor, Ireland</p>

  <ul class="contact">
    <li>00 353 (0) 41 55210
      <svg viewBox="0 0 20 18" aria-label="Phone"><path d="M2,7 C2,2 18,2 18,7 L14,7 L13,5 L7,5 L6,7 Z" fill="#fff"/><path d="M5,9 L15,9 L17,16 L3,16 Z" fill="#fff"/><circle cx="10" cy="12.5" r="2" fill="#1f844c"/></svg>
    </li>
    <li>00 353 (0) 41 55220
      <svg viewBox="0 0 20 18" aria-label="Fax"><rect x="5" y="1" width="10" height="5" fill="#fff"/><rect x="1" y="6" width="18" height="8" rx="2" fill="#fff"/><rect x="5" y="11" width="10" height="6" fill="#fff" stroke="#1f844c" stroke-width="1.2"/></svg>
    </li>
    <li>automation@dravel-example.ie
      <svg viewBox="0 0 20 18" aria-label="Email"><rect x="1" y="3" width="18" height="13" fill="#fff"/><path d="M1,3 L10,11 L19,3 M1,16 L8,9 M19,16 L12,9" fill="none" stroke="#1f844c" stroke-width="1.2"/></svg>
    </li>
  </ul>
</section>

<section class="card card-back">
  <div class="brand"><span class="brand-dot"></span>Dravel Automation</div>
  <div class="tagline">
    <p class="tagline-lead">Automated Equipment:</p>
    <p class="tagline-list">Design, Build, Control, Test, Support</p>
  </div>
</section>

</body>
</html>
```